Real Estate 2015 sold listings postcard

Real estate. I want one side to list 2015 sales. Mailing side with additional information. I am including a "concept" but it needs to be professionalized... Feel free to change color, fonts, layout, add watermark, whatever you think will work. Text on backside may be tweaked. I do want postcards addressed. How do i send mailing list or does Brightmark Press do that part?

NOTE: Postcard should be 8.5 x 5.5 inches.
Updates

postcard should be 8.5" x 5.5" size

Target Market(s)

Home owners who may want to sell

Industry/Entity Type

Real Estate Agent

Requirements
Must have
• The sold information and contact oinformation I have provided
Nice to have
• Watermark with my initials

```html
<!DOCTYPE html>
<html lang="en">
<head>
<meta charset="utf-8">
<title>2015 Sales Postcard – Harbor Crest Realtors</title>
<link rel="stylesheet" href="https://fonts.googleapis.com/css2?family=Roboto+Condensed:ital,wght@0,400;0,700;1,400;1,700&family=Montserrat:wght@500;600;700&family=Kaushan+Script&display=swap">
<style>
:root{
  --brand-blue:#1b5c9c;
  --header-blue:#1d63a8;
  --row-blue:#d3e8f7;
  --band-blue:#9fd1f2;
  --button-blue:#a9d2f3;
  --ink:#1d1d1d;
  --name-red:#d4262b;
  --gold:#c39b2a;
  --paper:#ffffff;
  --stage:#ebe7e2;
  --panel-grey:#d9d9d9;
}
*{box-sizing:border-box;margin:0;padding:0}
html,body{width:1200px;height:1000px;overflow:hidden}
body{background:var(--stage);position:relative;font-family:"Roboto Condensed",Arial,sans-serif;color:var(--ink)}
.card{position:absolute;background:var(--paper);box-shadow:0 2px 6px rgba(0,0,0,.18)}
.front{left:40px;top:28px;width:712px;height:460px}
.back{left:447px;top:511px;width:709px;height:488px;overflow:hidden}

/* front */
.brand-box{position:absolute;left:28px;top:12px;width:118px;height:52px;border:1px solid #c9c9c9;border-radius:6px;background:#fff;display:flex;align-items:center;justify-content:center;gap:5px}
.brand-box .mark{width:9px;height:9px;background:var(--gold)}
.brand-name{font-weight:700;font-size:11.5px;color:var(--ink);line-height:1.05;text-align:center}
.title-band{position:absolute;left:150px;top:20px;width:546px;height:32px;background:var(--header-blue);color:#fff;font-family:"Montserrat",sans-serif;font-weight:700;font-size:21px;line-height:32px;padding-left:12px;white-space:nowrap}
.title-rule{position:absolute;left:150px;top:56px;width:546px;height:2px;background:var(--header-blue)}
.sold-rule{position:absolute;left:14px;top:80px;width:682px;height:2px;background:#222}
.sold{position:absolute;left:313px;top:66px;padding:0 6px;background:#fff;font-family:"Montserrat",sans-serif;font-weight:700;font-size:25px;color:var(--brand-blue);border-left:2px solid #222;border-right:2px solid #222;line-height:28px}
.sales{position:absolute;left:15px;top:96px;width:682px;border-collapse:separate;border-spacing:0;font-size:11.5px}
.sales th{background:var(--header-blue);color:#fff;font-size:13px;font-weight:700;height:22px;text-align:left}
.sales th:first-child{border-radius:6px 0 0 6px;padding-left:12px}
.sales th:last-child{border-radius:0 6px 6px 0}
.sales td{height:15.5px;font-weight:700;text-align:center;padding:0;white-space:nowrap}
.sales td:first-child{text-align:left;padding-left:12px}
.sales tbody tr:nth-child(odd) td{background:var(--row-blue)}
.table-frame{position:absolute;left:15px;top:120px;width:682px;height:252px;border:1px solid #9aa8b4;border-radius:7px;pointer-events:none}
.agent-photo{position:absolute;left:108px;top:377px;width:57px;height:73px;border:1px solid #bbb;background:linear-gradient(180deg,#8a6a4a 0%,#c48c6e 45%,#c8242c 80%,#b0202a 100%)}
.agent-line{position:absolute;left:173px;top:379px;font-family:"Montserrat",sans-serif;font-weight:500;font-size:12.5px;white-space:nowrap;display:flex;align-items:baseline;gap:5px}
.agent-script{font-family:"Kaushan Script",cursive;color:var(--name-red);font-size:19px}
.contact-band{position:absolute;left:166px;top:406px;width:532px;height:27px;background:var(--band-blue);font-family:"Montserrat",sans-serif;font-weight:500;font-size:14px;color:var(--ink)}
.contact-item{position:absolute;top:0;height:27px;display:flex;align-items:center;gap:4px;white-space:nowrap}
.contact-email{left:10px}
.contact-phone{left:213px}
.contact-web{left:350px}
.disclaimer{position:absolute;left:185px;top:439px;font-size:8.5px;font-weight:700;white-space:nowrap}

/* back */
.back-top{position:absolute;left:0;top:0;width:343px;height:94px;background:linear-gradient(90deg,#e3e3e3,#f4f4f4)}
.back-left-bottom{position:absolute;left:0;top:398px;width:375px;height:90px;background:linear-gradient(90deg,#e8e8e8,#f3f3f3)}
.back-panel{position:absolute;left:375px;top:229px;width:334px;height:259px;background:var(--panel-grey)}
.stamp{position:absolute;left:599px;top:19px;width:88px;height:103px;border:1px solid #c6c6c6;background:#fff}
.back-brand{position:absolute;left:366px;top:30px;width:160px;display:flex;flex-direction:column;align-items:center;gap:3px}
.back-brand .row{display:flex;align-items:center;gap:6px}
.back-brand .mark{width:12px;height:12px;background:var(--gold)}
.back-brand .name{font-weight:700;font-size:16px;color:var(--ink)}
.back-brand .web{font-size:11px;display:flex;align-items:center;gap:3px;margin-top:5px}
.back-photo{position:absolute;left:363px;top:109px;width:86px;height:112px;background:linear-gradient(180deg,#7d5f45 0%,#c79276 40%,#c8242c 75%,#a81e27 100%)}
.agent-band{position:absolute;left:363px;top:166px;width:346px;height:55px;background:var(--brand-blue);border-radius:10px 0 0 0;color:#fff;padding:6px 0 0 91px;font-size:14.5px;line-height:22px;white-space:nowrap}
.agent-band .nm{font-weight:700;font-size:17px}
.pitch{position:absolute;left:32px;top:99px;width:320px}
.pitch h2{color:var(--brand-blue);font-size:17px;font-weight:700;line-height:20px;width:290px}
.checks{display:flex;gap:18px;font-style:italic;font-size:11.5px;margin-top:2px}
.checks span{display:flex;align-items:center;gap:2px}
.reach{font-style:italic;font-size:14px;margin-top:8px;white-space:nowrap}
.reach b{color:var(--brand-blue)}
.cta{margin-top:9px;width:304px;height:24px;border:1.5px solid #1f2f4a;border-radius:6px;background:var(--button-blue);font-size:14px;font-weight:700;text-align:center;line-height:21px;white-space:nowrap}
.cta em{font-style:normal;color:var(--brand-blue)}
.body-copy{margin-top:10px;font-size:9.6px;line-height:12.4px;width:308px;text-align:justify}
.body-copy p+p{margin-top:12px}
</style>
</head>
<body>

<section class="card front">
  <div class="brand-box"><span class="mark"></span><span class="brand-name">HARBOR CREST<br>REALTORS</span></div>
  <div class="title-band">2015 SALES IN YOUR NEIGHBORHOOD</div>
  <div class="title-rule"></div>
  <div class="sold-rule"></div>
  <div class="sold">SOLD</div>

  <table class="sales">
    <colgroup><col style="width:113px"><col style="width:32px"><col style="width:42px"><col style="width:78px"><col style="width:100px"><col style="width:82px"><col style="width:90px"><col style="width:80px"><col style="width:65px"></colgroup>
    <thead><tr><th>Address</th><th>BR</th><th>BA</th><th>SqFt</th><th>Lot Size</th><th>Lot Price</th><th>Sale Price</th><th>$/Sq. Ft</th><th>DOM</th></tr></thead>
    <tbody>
      <tr><td>387 Alder PL*</td><td>3</td><td>3 ½</td><td>2588</td><td>9239</td><td>3088000</td><td>3,100,000</td><td>1198</td><td>9</td></tr>
      <tr><td>3657 Hollis ST</td><td>4</td><td>3</td><td>2228</td><td>6147</td><td>2998000</td><td>3000000</td><td>1346</td><td>23</td></tr>
      <tr><td>261 Brookview DR</td><td>4</td><td>3</td><td>2185</td><td>7040</td><td>2500000</td><td>2925000</td><td>1,339</td><td>9</td></tr>
      <tr><td>437 Linden AVE*</td><td>4</td><td>2</td><td>1611</td><td>13,237</td><td>2498000</td><td>2610000</td><td>1620</td><td>8</td></tr>
      <tr><td>4123 Marlow AVE*</td><td>4</td><td>2</td><td>2227</td><td>8700</td><td>2295000</td><td>2595000</td><td>1165</td><td>8</td></tr>
      <tr><td>76 Whitman CIR*</td><td>3</td><td>2</td><td>1364</td><td>5917</td><td>1788000</td><td>2525000</td><td>1851</td><td>8</td></tr>
      <tr><td>3665 Sorrel CIR</td><td>4</td><td>2</td><td>1646</td><td>6404</td><td>2500000</td><td>2475000</td><td>1504</td><td>18</td></tr>
      <tr><td>410 Canyon PL*</td><td>3</td><td>2</td><td>1674</td><td>11200</td><td>2498000</td><td>2450000</td><td>1464</td><td>16</td></tr>
      <tr><td>291 Brookview DR*</td><td>4</td><td>2</td><td>1690</td><td>8178</td><td>2199000</td><td>240000</td><td>1420</td><td>7</td></tr>
      <tr><td>303 Brookview DR</td><td>3</td><td>2</td><td>1674</td><td>8538</td><td>2200000</td><td>2260000</td><td>1350</td><td>97</td></tr>
      <tr><td>93 Whitman CIR</td><td>3</td><td>2</td><td>1243</td><td>6080</td><td>1488000</td><td>2250000</td><td>1810</td><td>7</td></tr>
      <tr><td>3702 Preston CIR*</td><td>4</td><td>2</td><td>13333</td><td>6493</td><td>1895000</td><td>2227500</td><td>1671</td><td>6</td></tr>
      <tr><td>372 Meadow DR*</td><td>3</td><td>2</td><td>1740</td><td>6324</td><td>2200000</td><td>2180000</td><td>1,253</td><td>12</td></tr>
      <tr><td>3647 Hollis ST</td><td>4</td><td>2</td><td>1474</td><td>6111</td><td>1799900</td><td>2115000</td><td>1,435</td><td>17</td></tr>
      <tr><td>60 Whitman CIR</td><td>4</td><td>2</td><td>1456</td><td>6111</td><td>1788000</td><td>2000000</td><td>1374</td><td>11</td></tr>
      <tr><td>252 Ashford CT</td><td>3</td><td>2</td><td>1428</td><td>10,624</td><td>1,950,000</td><td>2,100,000</td><td>1471</td><td>20</td></tr>
    </tbody>
  </table>
  <div class="table-frame"></div>

  <div class="agent-photo" role="img" aria-label="Portrait photo of agent Dana Whitfield"></div>
  <div class="agent-line"><span class="agent-script">Dana Whitfield</span><span>| Relocation Specialist | California Licence #00412873</span></div>
  <div class="contact-band">
    <span class="contact-item contact-email"><svg width="16" height="12" viewBox="0 0 16 12"><rect x="0.75" y="0.75" width="14.5" height="10.5" fill="none" stroke="#1b5c9c" stroke-width="1.5"/><path d="M1 1l7 6 7-6" fill="none" stroke="#1b5c9c" stroke-width="1.5"/></svg>dana@hcrealty.com</span>
    <span class="contact-item contact-phone"><svg width="10" height="17" viewBox="0 0 10 17"><rect x="0.75" y="0.75" width="8.5" height="15.5" rx="1.5" fill="none" stroke="#1b5c9c" stroke-width="1.5"/><rect x="2.5" y="3" width="5" height="9" fill="#1b5c9c"/></svg>650-555-0148</span>
    <span class="contact-item contact-web"><svg width="12" height="12" viewBox="0 0 12 12"><circle cx="6" cy="6" r="5.2" fill="none" stroke="#1b5c9c" stroke-width="1.2"/><ellipse cx="6" cy="6" rx="2.3" ry="5.2" fill="none" stroke="#1b5c9c" stroke-width="1"/><path d="M1 6h10" stroke="#1b5c9c" stroke-width="1"/></svg>www.dwhitfield.com</span>
  </div>
  <p class="disclaimer">*indicates Harbor Crest Realtors listing or sale. This information is deemed reliable, but not verified or guaranteed</p>
</section>

<section class="card back">
  <div class="back-top"></div>
  <div class="back-left-bottom"></div>
  <div class="back-panel"></div>
  <div class="stamp"></div>

  <div class="back-brand">
    <div class="row"><span class="mark"></span><span class="name">HARBOR CREST</span></div>
    <div class="web"><svg width="10" height="10" viewBox="0 0 12 12"><circle cx="6" cy="6" r="5.2" fill="none" stroke="#1b5c9c" stroke-width="1.2"/><ellipse cx="6" cy="6" rx="2.3" ry="5.2" fill="none" stroke="#1b5c9c" stroke-width="1"/><path d="M1 6h10" stroke="#1b5c9c" stroke-width="1"/></svg>www.dwhitfield.com</div>
  </div>

  <div class="agent-band">
    <div><span class="nm">DANA WHITFIELD</span> &nbsp;|&nbsp; License: 00412873</div>
    <div>650-555-0148 &nbsp;|&nbsp; dana@hcrealty.com</div>
  </div>
  <div class="back-photo" role="img" aria-label="Portrait photo of agent Dana Whitfield in a red jacket"></div>

  <div class="pitch">
    <h2>Traditionally, Feb. through April are the best months to sell</h2>
    <div class="checks">
      <span><svg width="10" height="10" viewBox="0 0 10 10"><rect x="0.5" y="0.5" width="9" height="9" fill="#fff" stroke="#1b5c9c"/><path d="M2 5l2 2 4-5" fill="none" stroke="#1b5c9c" stroke-width="1.6"/></svg>Most Offers</span>
      <span><svg width="10" height="10" viewBox="0 0 10 10"><rect x="0.5" y="0.5" width="9" height="9" fill="#fff" stroke="#1b5c9c"/><path d="M2 5l2 2 4-5" fill="none" stroke="#1b5c9c" stroke-width="1.6"/></svg>Higest Prices</span>
    </div>
    <p class="reach">Our Listings are advertised locally and <b>in 40 countries!!</b></p>
    <div class="cta"><em>Don't Wait.</em> Call Now for a Private Consultation!</div>
    <div class="body-copy">
      <p>Our market continues to be strong, which reflects both our vibrant and growing local economy and our seemingly chronic shortage of inventory. As long as those conditions continue, our market values will remain high. That is good news to sellers who may want to down-size or move to a different area for a new job, or maybe to be closer to family.</p>
      <p>I am a Harbor Crest Realtors certified Relocation Specialist, and, as such, I can connect you with experienced and professional real estate agent anywhere in the country and in most countries around the world. We can co-ordinate your transactions at both ends, making your transition as seamless as possible. If you are planning a move, across the street or across the county, call me now for a confidential consultation.</p>
    </div>
  </div>
</section>

</body>
</html>
```